Refer a Friend A5 Flyer for Healthcare Staff

We need an A5 flyer that we can hand out to existing and new staff members promoting our Refer a friend Scheme. We need the leaflet to encourage staff to talk to their family and friends about joining our Healthcare Agency, which provides staff to local care related establishments. Using our logo and brand colours blue and green, as per our website, the final design will need to clearly convey the benefits and attractions of referring additional staff to the team. In addition is the promotion of our Chatterly page, requesting staff to like the page and to like and share various posts.

Target Market(s)

Healthcare and potential Healthcare Staff

Industry/Entity Type

Healthcare

Colors
33b8a4
3277b5

Requirements
Must have
• Company Logo, Brand colours,
• text; "Refer a Friend and receive a £50 Bonus after just 1 completed shift"
• text; "3 easy steps to refer a friend, 1 Fill out your name on the back of your Business Card 2 Hand the card to your friend or any person you wish to refer, 3 ask your friend to present the card to us when they attend their interview"
• text; "Like and share any of our Open Days on Chatterly for a chance to win a prize, you can find us easily by searching @CarewellPlacementGroup"
• text; "Like our Page to stay up to date with our events and offers"
Nice to have
• care worker / elderly care / support worker pictures
• Content / pics from website www.carewellplacementgroup.co.uk

```html
<!DOCTYPE html>
<html lang="en">
<head>
<meta charset="utf-8">
<title>Refer a Friend Flyer</title>
<link rel="stylesheet" href="https://fonts.googleapis.com/css2?family=Montserrat:wght@400;500;600;700;800&display=swap">
<style>
  :root{
    --bg:#d4d5d7;
    --paper:#f8f9fb;
    --teal:#6fcbba;
    --teal-soft:#88d5c7;
    --teal-badge:#17a98c;
    --teal-deep:#0f8a6c;
    --blue:#0050a2;
    --ink:#4a4a4a;
    --white:#ffffff;
  }
  *{margin:0;padding:0;box-sizing:border-box}
  html,body{width:1200px;height:1200px;overflow:hidden;background:var(--bg)}
  body{font-family:"Montserrat",sans-serif;position:relative}
  .flyer{position:absolute;left:250px;top:104px;width:700px;height:992px;background:var(--paper);overflow:hidden}
  .shapes{position:absolute;inset:0;width:700px;height:992px}
  .logo{position:absolute;left:0;top:0;width:161px;height:70px;background:var(--white);border-radius:0 0 4px 0;display:flex;align-items:center;gap:7px;padding-left:14px}
  .logo-dot{width:12px;height:12px;border-radius:50%;background:var(--teal-badge);flex:none}
  .logo-name{font-weight:600;font-size:14px;line-height:16px;color:var(--blue)}
  .steps-title{position:absolute;right:26px;top:250px;text-align:right;font-weight:700;font-size:31px;line-height:39.5px;color:var(--ink)}
  .steps-rule{position:absolute;left:433px;top:376px;width:234px;height:3px;background:var(--ink)}
  .step{position:absolute;left:297px;display:flex;align-items:center}
  .step-num{width:46px;height:46px;border-radius:50%;background:var(--teal-badge);color:var(--white);font-weight:800;font-size:26px;display:flex;align-items:center;justify-content:center;flex:none}
  .step-text{margin-left:14px;font-size:18.5px;line-height:33px;color:var(--ink);letter-spacing:.2px;white-space:nowrap}
  .offer{position:absolute;left:0;width:290px;text-align:center;font-weight:800;font-size:25px;color:var(--ink)}
  .offer .accent{color:var(--blue)}
  .bonus{position:absolute;left:0;width:290px;text-align:center;font-weight:700;font-size:25px;line-height:37px;color:var(--teal-deep)}
  .bonus .star{color:var(--blue)}
  .share-copy{position:absolute;right:14px;top:736px;text-align:right;font-weight:600;font-size:19.5px;line-height:27.8px;color:var(--white)}
  .share-copy b,.like-copy b{font-weight:800}
  .rule-light{position:absolute;left:180px;top:869px;width:504px;height:2px;background:var(--white)}
  .like-copy{position:absolute;left:180px;top:897px;font-weight:600;font-size:19.5px;line-height:28px;color:var(--white)}
  .footer-info{position:absolute;left:180px;top:958px;font-size:10.5px;color:var(--white);letter-spacing:.2px}
</style>
</head>
<body>
  <main class="flyer">
    <svg class="shapes" viewBox="0 0 1126 1597" preserveAspectRatio="none">
      <defs>
        <linearGradient id="photoTone" x1="0" y1="0" x2="1" y2="1">
          <stop offset="0" stop-color="#e4e9ef"/>
          <stop offset=".5" stop-color="#9fc3e2"/>
          <stop offset="1" stop-color="#d8e2ec"/>
        </linearGradient>
      </defs>
      <path role="img" aria-label="Photo of a care worker in blue scrubs pointing out a window beside an elderly man in a wheelchair" fill="url(#photoTone)" d="M0,0 H1126 V180 L480,560 Q380,625 290,615 L0,490 Z"/>
      <path fill="var(--teal)" d="M0,490 L290,615 Q380,625 480,560 L1126,180 V340 L560,660 Q380,780 230,700 L0,565 Z"/>
      <path fill="var(--teal-soft)" d="M0,702 L190,812 Q255,850 255,930 V1190 Q255,1262 190,1300 L0,1378 Z"/>
      <path fill="var(--blue)" d="M0,1462 L720,1055 Q830,1000 940,1055 L1126,1150 V1597 H0 Z"/>
      <circle cx="778" cy="1131" r="32" fill="none" stroke="#fff" stroke-width="2.5"/>
      <path d="M778,1150 L760,1132 Q752,1120 763,1113 Q772,1108 778,1118 Q784,1108 793,1113 Q804,1120 796,1132 Z" fill="none" stroke="#fff" stroke-width="2.5"/>
      <circle cx="878" cy="1131" r="32" fill="none" stroke="#fff" stroke-width="2.5"/>
      <g fill="none" stroke="#fff" stroke-width="2.5">
        <circle cx="890" cy="1113" r="5"/><circle cx="864" cy="1131" r="5"/><circle cx="890" cy="1149" r="5"/>
        <path d="M868,1128 L886,1116 M868,1134 L886,1146"/>
      </g>
      <circle cx="200" cy="1492" r="62" fill="none" stroke="#fff" stroke-width="4"/>
      <circle cx="200" cy="1492" r="52" fill="none" stroke="#fff" stroke-width="3"/>
      <path d="M176,1494 L194,1512 L226,1474" fill="none" stroke="#fff" stroke-width="6" stroke-linecap="round" stroke-linejoin="round"/>
    </svg>

    <div class="logo">
      <span class="logo-dot"></span>
      <span class="logo-name">Carewell<br>Placement</span>
    </div>

    <h2 class="steps-title">3 EASY STEP<br>TO REFERENCE<br>A FRIEND</h2>
    <div class="steps-rule"></div>

    <div class="step" style="top:387px"><span class="step-num">1</span><p class="step-text">Fill in your name on the back of<br>your business card</p></div>
    <div class="step" style="top:464px"><span class="step-num">2</span><p class="step-text">Give the card to your friend or<br>the person you want to refer to</p></div>
    <div class="step" style="top:544px"><span class="step-num">3</span><p class="step-text">Ask your friend to give us a card<br>when they attend their interview</p></div>

    <p class="offer" style="top:505px">REFER A FRIEND</p>
    <p class="offer" style="top:542px">and</p>
    <p class="offer" style="top:583px;font-size:26px"><span class="accent">RECEIVE</span> A <span class="accent">£ 50</span></p>

    <p class="bonus" style="top:663px"><span class="star">*</span>Bonus after only<br>1 shift complete</p>

    <p class="share-copy"><b>LIKE</b> and <b>SHARE</b> our open day on<br>Chatterly for a chance to win prizes, you<br>can find us easily by searching on<br>@CarewellPlacementGroup</p>

    <div class="rule-light"></div>

    <p class="like-copy"><b>LIKE</b> our page to get the<br>latest infromation about our events and offers</p>
    <p class="footer-info">FOR MORE INFORMATION www.carewellplacementgroup.co.uk</p>
  </main>
</body>
</html>
```